Brightfold Partners Website

Brightfold Partners Advisory Services is a company which provides specialised advise in carbon markets, climate policy, landscapes, resilience and change. We are based in Australia but the majority of our business is global. Our clients range from governments to large corporates and not for profit organisations.
Our focus is on developing the capabilities of government officials, business decision makers and land managers so they can better navigate the complexity of climate change and sustainability.
We are looking for a website that is consistent with the high end professional services which we provide to serious players.
I have attached two versions of our logo. I have also attached the back of our business card so you can get a sense of what we hand to potential clients.

Target Market(s)

Professional individuals, decision makers, board members etc, government officials.

Industry/Entity Type

Government

Number of Pages Required

4 page

Font styles to use
Serif
Sans Serif

Requirements
Must have
• Please provide
• 1. Home page
• 2. Service page template
• 3. Contact page
• 4. Lead expert profile page

```html
<!DOCTYPE html>
<html lang="en">
<head>
<meta charset="utf-8">
<title>Brightfold Partners – Services</title>
<link rel="stylesheet" href="https://fonts.googleapis.com/css2?family=Cinzel:wght@600;700&family=Open+Sans:wght@300;400&family=Tinos&display=swap">
<style>
  :root {
    --header-dark: #362d2b;
    --accent-blue: #4f8fc9;
    --footer-teal: #4a9bb1;
    --body-text: #222222;
    --white: #ffffff;
    --sky-top: #3f82c4;
    --sky-mid: #a9c8e4;
    --hill: #5a6f7d;
    --grass: #5d6a3c;
  }
  * { box-sizing: border-box; margin: 0; padding: 0; }
  html, body { width: 1200px; height: 1091px; overflow: hidden; background: var(--white); }
  .page { position: relative; width: 1200px; height: 1091px; }

  .site-header { position: absolute; left: 0; top: 0; width: 1200px; height: 178px; background: var(--header-dark); }
  .brand-box {
    position: absolute; left: 541px; top: 0; width: 118px; height: 117px; background: var(--white);
    display: flex; flex-direction: column; align-items: center; justify-content: center; gap: 8px;
  }
  .brand-dot { width: 22px; height: 22px; border-radius: 50%; background: var(--header-dark); }
  .brand-name {
    font-family: "Tinos", serif; font-size: 14px; letter-spacing: 1.5px; line-height: 17px;
    color: var(--header-dark); text-align: center;
  }
  .contact-lines {
    position: absolute; right: 97px; top: 37px; text-align: right;
    font-family: "Open Sans", sans-serif; font-size: 14px; line-height: 21px; color: var(--white);
  }
  .main-nav { position: absolute; left: 324px; top: 133px; display: flex; gap: 30px; }
  .main-nav a {
    font-family: "Open Sans", sans-serif; font-weight: 300; font-size: 21px; color: var(--white);
    text-decoration: none; letter-spacing: -0.2px;
  }
  .social-links { position: absolute; left: 997px; top: 126px; display: flex; gap: 9px; }
  .social-links span { width: 29px; height: 29px; border: 2px solid var(--white); border-radius: 50%; }

  .accent-rule { position: absolute; left: 0; top: 178px; width: 1200px; height: 7px; background: var(--accent-blue); border-bottom: 2px solid var(--header-dark); }

  .hero {
    position: absolute; left: 0; top: 187px; width: 1200px; height: 502px;
    background: linear-gradient(180deg, var(--sky-top) 0%, var(--sky-mid) 55%, var(--hill) 78%, var(--grass) 88%, #4b5830 100%);
  }
  .hero-title {
    position: absolute; left: 97px; top: 70px;
    font-family: "Cinzel", serif; font-weight: 700; font-size: 28px; line-height: 37px;
    color: var(--white); letter-spacing: 0.6px;
  }
  .hero-focus {
    position: absolute; left: 97px; top: 183px;
    font-family: "Cinzel", serif; font-weight: 700; font-size: 19px; line-height: 25px;
    color: var(--white); letter-spacing: 0.3px;
  }

  .content {
    position: absolute; left: 97px; top: 712px; width: 1020px;
    font-family: "Tinos", serif; font-size: 18.7px; line-height: 22px; color: var(--body-text);
  }
  .content p { margin-bottom: 22px; }
  .content a { color: var(--body-text); text-decoration: underline; }
  .engagement-list { list-style: none; }

  .site-footer {
    position: absolute; left: 0; top: 1050px; width: 1200px; height: 41px; background: var(--footer-teal);
    font-family: "Open Sans", sans-serif; font-size: 15px; color: var(--white);
    display: flex; align-items: center; justify-content: center; gap: 10px;
  }
</style>
</head>
<body>
<div class="page">
  <header class="site-header">
    <div class="brand-box">
      <span class="brand-dot"></span>
      <span class="brand-name">BRIGHTFOLD<br>PARTNERS</span>
    </div>
    <div class="contact-lines">
      <div>+61 400 555 123</div>
      <div>daniel.hart@brightfoldpartners.com.au</div>
    </div>
    <nav class="main-nav">
      <a href="#">HOME</a><a href="#">ABOUT US</a><a href="#">PROFILES</a><a href="#">SERVICES</a><a href="#">CONTACT US</a>
    </nav>
    <div class="social-links"><span></span><span></span><span></span></div>
  </header>
  <div class="accent-rule"></div>

  <section class="hero" role="img" aria-label="Photograph of wind turbines on green hills under a blue sky">
    <h1 class="hero-title">Brightfold Partners provides expert advisory services<br>in carbon markets, climate policy, landscapes and change.</h1>
    <p class="hero-focus">Our focus is on developing the capabilities of government officials,<br>business decision makers and land managers so they can better navigate<br>the complexity of climate change &amp; sustainability.</p>
  </section>

  <main class="content">
    <p>Daniel Hart leads all of Brightfold Partners's advisory engagements.&nbsp; His profile is available <a href="#">here</a>.</p>
    <p>We provide advisory services across a number of specialised areas.&nbsp; However, all of our advisory services are tailored to<br>the situation and needs of the client, so no two engagements are the same.</p>
    <div>A selection of recent engagements is provided below.</div>
    <ul class="engagement-list">
      <li><a href="#">Corporate Advisory on Carbon Markets</a></li>
      <li><a href="#">Project Mechanisms (carbon credits &amp; offsets)</a></li>
      <li><a href="#">Monitoring, Reporting &amp; Verification</a></li>
      <li><a href="#">Institutional Arrangements</a></li>
      <li><a href="#">Training &amp; Coaching</a></li>
      <li><a href="#">China's Carbon Markets</a></li>
    </ul>
    <p style="margin-top:22px">Please <a href="#">contact us</a> if you would like to explore how Brightfold Partners can support your efforts in climate change &amp; sustainability.</p>
  </main>

  <footer class="site-footer">
    <span>© 2014 Brightfold Partners Advisory Services</span><span>|</span><span>Terms and Conditions</span><span>|</span><span>Disclaimer</span>
  </footer>
</div>
</body>
</html>
```